Business Card Layout front and back

In need of business cards for my company.

Please look around TwistedLanyard.com for inspiration

Needs to have the following info

Phone number
Hours
website (all of which can be found on the site)
facebook.com/user/twistedlanyard
youtube.com/user/TwistedLanyard
www.twitter.com/twistedlanyard
to go along with the social media, i would like their appropriate logos next to each or incorporated somehow
Dale Pembrook
Owner / Grunt
Logo
Somewhere it needs to say "Veteran Owned and Operated"

I also have a group on facebook called Knot Ahead! I would like this to be prominent on the back of the card. "Get in the discussion at facebook.com/groups/KnotAhead"

Please be creative. I have attached the logo.eps file. Please feel free to use any pictures on any of my sites.

Thanks,
Dale

```html
<!DOCTYPE html>
<html lang="en">
<head>
<meta charset="utf-8">
<title>Twisted Lanyard — Business Card Front and Back</title>
<link rel="stylesheet" href="https://fonts.googleapis.com/css2?family=Open+Sans:wght@300;400;600;700;800&display=swap">
<style>
  :root {
    --canvas: #e8e5df;
    --lime: #a6d12a;
    --lime-dark: #8cb31c;
    --paper: #f4f4f2;
    --ink: #262626;
    --slate: #3b3b3d;
    --slate-deep: #2a2a2c;
    --steel: #5a5a5d;
    --muted: #8a8a8a;
    --light-text: #e6e6e6;
  }
  * { box-sizing: border-box; margin: 0; padding: 0; }
  html, body {
    width: 1200px; height: 1023px; overflow: hidden;
    background: var(--canvas);
    font-family: "Open Sans", Arial, sans-serif;
  }
  .card {
    position: absolute; top: 160px;
    width: 400px; height: 700px;
    background: var(--paper);
    overflow: hidden;
    box-shadow: 0 10px 30px rgba(0,0,0,0.18);
  }
  .card--front { left: 160px; }
  .card--back { left: 640px; }

  .edge { position: absolute; left: 0; right: 0; background: var(--lime); }
  .edge--top { top: 0; height: 16px; }
  .edge--bottom { bottom: 0; height: 30px; border-top: 3px solid var(--lime-dark); }

  /* Front: identity */
  .identity { position: absolute; top: 16px; left: 0; right: 0; height: 344px; padding: 46px 34px 0; text-align: right; }
  .brand { font-weight: 800; font-size: 56px; line-height: 0.95; color: var(--ink); text-transform: uppercase; letter-spacing: -1px; }
  .person { margin-top: 56px; font-size: 34px; color: #3a3a3a; text-transform: uppercase; letter-spacing: 0.5px; }
  .person__first { font-weight: 800; }
  .person__last { font-weight: 300; }
  .role { margin-top: 6px; font-size: 15px; letter-spacing: 3px; color: var(--muted); text-transform: uppercase; }

  /* Front: contact band */
  .contact { position: absolute; top: 360px; left: 0; right: 0; height: 200px;
    background: linear-gradient(160deg, var(--slate) 0%, var(--slate-deep) 100%); padding: 22px 26px 0; }
  .tagline { font-size: 21px; font-weight: 600; color: var(--lime); margin-bottom: 22px; }
  .row { display: flex; align-items: flex-start; gap: 22px; }
  .icon { flex: 0 0 46px; width: 46px; height: 46px; }
  .lines { font-size: 15px; line-height: 1.45; color: var(--light-text); }

  .web { position: absolute; top: 560px; left: 0; right: 0; height: 100px;
    background: var(--steel); padding: 12px 26px 0; }
  .web .lines { font-size: 13.5px; line-height: 1.5; }
  .link { display: flex; align-items: center; gap: 7px; white-space: nowrap; }
  .link__mark { width: 9px; height: 9px; background: var(--light-text); border-radius: 2px; }
  .link__mark--blank { background: transparent; }

  .gap { position: absolute; top: 660px; left: 0; right: 0; height: 10px; background: var(--paper); }

  /* Back */
  .back-field { position: absolute; top: 0; left: 0; right: 0; height: 520px;
    background: linear-gradient(160deg, var(--slate) 0%, var(--slate-deep) 100%); }
  .discussion { position: absolute; top: 520px; left: 0; right: 0; height: 150px;
    display: flex; flex-direction: column; justify-content: center; padding: 0 30px; color: var(--ink); }
  .discussion__lead { font-size: 20px; font-weight: 400; }
  .discussion__url { font-size: 20px; font-weight: 600; margin-top: 4px; white-space: nowrap; }
</style>
</head>
<body>

<section class="card card--front" aria-label="Business card front">
  <div class="edge edge--top"></div>

  <header class="identity">
    <div class="brand">Twisted<br>Lanyard</div>
    <div class="person"><span class="person__first">Dale</span> <span class="person__last">Pembrook</span></div>
    <div class="role">Owner / Grunt</div>
  </header>

  <div class="contact">
    <p class="tagline">Veteran Owned and Operated</p>
    <div class="row">
      <svg class="icon" viewBox="0 0 46 46" aria-hidden="true">
        <path d="M6 16 Q23 4 40 16 L36 22 L30 19 L30 15 Q23 12 16 15 L16 19 L10 22 Z" fill="#9a9a9c"/>
        <rect x="10" y="24" width="26" height="16" rx="3" fill="#9a9a9c"/>
        <circle cx="23" cy="32" r="4.5" fill="#3b3b3d"/>
      </svg>
      <div class="lines">
        555-014-2287<br>
        Monday - Friday 9:00AM - 6:00PM<br>
        Saturday and Sunday 9:00AM - 9:00PM<br>
        (Eastern Time)
      </div>
    </div>
  </div>

  <div class="web">
    <div class="row">
      <svg class="icon" viewBox="0 0 46 46" aria-hidden="true">
        <g fill="none" stroke="#cfcfd1" stroke-width="2.5">
          <circle cx="23" cy="23" r="18"/>
          <ellipse cx="23" cy="23" rx="8" ry="18"/>
          <line x1="5" y1="23" x2="41" y2="23"/>
          <path d="M8 14 H38 M8 32 H38"/>
        </g>
      </svg>
      <div class="lines">
        <div class="link"><span class="link__mark link__mark--blank"></span>www.TwistedLanyard.com</div>
        <div class="link"><span class="link__mark"></span>friendspace.com/user/twistedlanyard</div>
        <div class="link"><span class="link__mark"></span>clipstream.com/user/TwistedLanyard</div>
        <div class="link"><span class="link__mark"></span>www.chirpline.com/twistedlanyard</div>
      </div>
    </div>
  </div>

  <div class="gap"></div>
  <div class="edge edge--bottom"></div>
</section>

<section class="card card--back" aria-label="Business card back">
  <div class="back-field"></div>
  <div class="discussion">
    <p class="discussion__lead">Get in the discussion at</p>
    <p class="discussion__url">friendspace.com/groups/KnotAhead</p>
  </div>
  <div class="edge edge--bottom"></div>
</section>

</body>
</html>
```